Letterhead and Stationary for Construction Company

Lumen Forge needs modern Letterhead, Envelopes and Notepad designs.

Industry/Entity Type

Construction

Colors
f78f20
34a7d8
ffffff

Requirements
Must have
• Modern looking design.

```html
<!DOCTYPE html>
<html lang="en">
<head>
<meta charset="utf-8">
<title>Lumen Forge Stationery</title>
<link href="https://fonts.googleapis.com/css2?family=Source+Sans+3:wght@400;600&display=swap" rel="stylesheet">
<style>
  :root {
    --stage: #131313;
    --paper: #f4f3f1;
    --orange: #ef7a26;
    --blue: #1d6fb6;
    --ink: #4a4a4a;
    --rule: #8c8c8c;
    --spiral: #1a1a1a;
  }
  * { margin: 0; padding: 0; box-sizing: border-box; }
  html, body { width: 1200px; height: 750px; overflow: hidden; background: var(--stage); }
  body { position: relative; font-family: "Source Sans 3", sans-serif; color: var(--ink); }

  .brand { position: absolute; display: flex; align-items: center; gap: 4px; color: var(--blue); font-weight: 600; letter-spacing: -0.3px; white-space: nowrap; }
  .brand-dot { border-radius: 50%; background: var(--orange); flex: none; }

  /* Letterhead */
  .letterhead { position: absolute; left: 36px; top: 32px; width: 486px; height: 686px; background: var(--paper); overflow: hidden; }
  .letterhead .brand { left: 50%; top: 56px; transform: translateX(-50%); font-size: 22px; }
  .letterhead .brand-dot { width: 12px; height: 12px; }
  .salutation { position: absolute; left: 48px; top: 190px; font-size: 13.6px; line-height: 17px; color: #444; }
  .letter-body { position: absolute; left: 48px; top: 232px; width: 392px; font-size: 7.9px; line-height: 11.7px; text-align: justify; }
  .letter-body p { margin-bottom: 11.7px; }
  .closing { position: absolute; left: 48px; top: 478px; font-size: 7.9px; line-height: 11px; }
  .signature { position: absolute; left: 46px; top: 496px; width: 64px; height: 24px; background: #d9d8d6; border-radius: 2px; }
  .signer { position: absolute; left: 51px; top: 532px; font-size: 8.6px; line-height: 13px; }
  .corner { position: absolute; right: 0; bottom: 0; }
  .letter-contact { position: absolute; right: 15px; bottom: 14px; text-align: right; color: #fff; font-size: 8.6px; line-height: 11.6px; }
  .letter-contact .addr { margin-bottom: 3px; }
  .contact-row { display: flex; justify-content: flex-end; align-items: center; gap: 6px; }
  .contact-row svg { width: 7px; height: 7px; }

  /* Notepads */
  .notepad { position: absolute; background: var(--paper); }
  .notepad-wide { left: 586px; top: 80px; width: 298px; height: 226px; }
  .notepad-tall { left: 935px; top: 56px; width: 183px; height: 262px; }
  .binding { position: absolute; left: 0; top: 0; width: 100%; height: 20px; }
  .notepad .rule { position: absolute; height: 1px; background: var(--rule); }
  .notepad-wide .brand { left: 19px; top: 50px; font-size: 17px; }
  .notepad-wide .brand-dot { width: 9px; height: 9px; }
  .notepad-tall .brand { left: 50%; top: 34px; transform: translateX(-50%); font-size: 11.5px; }
  .notepad-tall .brand-dot { width: 6px; height: 6px; }

  /* Envelope back */
  .envelope-back { position: absolute; left: 613px; top: 358px; width: 545px; height: 250px; background: var(--paper); }
  .flap { position: absolute; left: 0; top: 0; }
  .flap-web { position: absolute; left: 0; width: 100%; top: 20px; text-align: center; color: #fff; font-size: 7.6px; letter-spacing: 2px; transform: rotate(180deg); }
  .flap-mark { position: absolute; left: 257px; top: 38px; width: 32px; height: 32px; border: 3px solid #fff; border-radius: 50%; }

  /* Envelope front */
  .envelope-front { position: absolute; left: 545px; top: 469px; width: 547px; height: 249px; background: var(--paper); overflow: hidden; box-shadow: 2px 2px 6px rgba(0,0,0,.25); }
  .envelope-front .brand { left: 25px; top: 50px; font-size: 21px; }
  .envelope-front .brand-dot { width: 11px; height: 11px; }
  .return-address { position: absolute; left: 25px; top: 84px; font-size: 8.8px; line-height: 10.2px; color: #333; }
  .front-web { position: absolute; right: 20px; bottom: 17px; color: #fff; font-size: 8.2px; letter-spacing: 1.6px; }
</style>
</head>
<body>

<section class="letterhead">
  <div class="brand"><span class="brand-dot"></span>lumenforge</div>
  <p class="salutation">Dear Mr. Harlow,</p>
  <div class="letter-body">
    <p>Lorem ipsum dolor sit amet, consectetur adipiscing elit. Donec orci purus, luctus vitae dignissim eu, iaculis sed purus. Vivamus faucibus, ipsum nec aliquet viverra, leo mauris condimentum ligula, sit amet sagittis enim ligula quis arcu. Nam egestas tortor id nisi porttitor mattis. In tortor ante, ultricies in suscipit a, tempus non massa. Vivamus et auctor mi. Fusce vel massa nulla. Phasellus nec eros mauris, et scelerisque orci.</p>
    <p>Donec malesuada orci vitae nulla accumsan porta a id massa. Quisque accumsan iaculis magna sit amet fringilla. Maecenas consequat, magna eget tincidunt semper, odio nibh rutrum mi, id feugiat ante nisi eu risus. Vestibulum nunc orci, rhoncus a placerat in, ultricies in mi. Cras mattis varius eros, vel fringilla nisi suscipit eget. Quisque scelerisque sagittis nulla at porttitor.</p>
    <p>Sed id augue vitae urna euismod commodo aliquet a quam. Pellentesque arcu velit, cursus et malesuada ut, consequat et diam. Nullam erat sem, rhoncus id ullamcorper vitae, rhoncus et arcu. In ultricies ultricies nulla, ut rutrum nisi iaculis at. Donec eu magna a metus ornare faucibus. Fusce aliquet faucibus ultricies. Morbi semper, est id tincidunt gravida, sem arcu adipiscing lacus, ac bibendum nulla leo eu purus. Quisque nec diam sed risus consectetur a accumsan quis quis nibh. Vestibulum id purus lorem.</p>
    <p>It is a long established fact that a reader will be distracted by the readable content of a page when looking at its layout. The point of using Lorem Ipsum is that it has a more-or-less normal distribution of letters, as opposed to using 'Content here, content here', making it look like readable English. Many desktop publishing packages</p>
  </div>
  <p class="closing">Sincerely,</p>
  <div class="signature" role="img" aria-label="Handwritten signature"></div>
  <p class="signer">Dana Whitcombe<br>CEO/ Founder</p>
  <svg class="corner" width="170" height="130" viewBox="0 0 170 130">
    <path d="M0 130 C20 55 85 2 170 0 V130 Z" fill="var(--orange)"/>
    <path d="M4 130 C24 58 88 5 170 3 V130 Z" fill="var(--blue)"/>
  </svg>
  <div class="letter-contact">
    <div class="addr">412 Copperfield Road<br>Brookhaven, Oregon 97021</div>
    <div class="contact-row">503 218 4476 <svg viewBox="0 0 10 10"><path d="M2 1 L4 1 L5 3.5 L3.8 4.5 Q5 6.5 6 6.8 L7 5.5 L9 6.5 L9 8.5 Q5 9.5 1 4 Z" fill="#fff"/></svg></div>
    <div class="contact-row">503 771 9025 <svg viewBox="0 0 10 10"><rect x="2.5" y="0.5" width="5" height="9" rx="1" fill="none" stroke="#fff" stroke-width="1.2"/></svg></div>
    <div class="contact-row">hello@lumenforge.co <svg viewBox="0 0 10 10"><rect x="0.5" y="2" width="9" height="6" fill="#fff"/><path d="M0.5 2 L5 5.5 L9.5 2" fill="none" stroke="var(--blue)" stroke-width="0.9"/></svg></div>
    <div class="contact-row">www.lumenforge.co <svg viewBox="0 0 10 10"><circle cx="5" cy="5" r="4.5" fill="#fff"/></svg></div>
  </div>
</section>

<section class="notepad notepad-wide">
  <svg class="binding" viewBox="0 0 298 20" preserveAspectRatio="none">
    <defs><pattern id="ring-wide" width="12.6" height="20" patternUnits="userSpaceOnUse"><rect x="2" y="0" width="2" height="14" fill="var(--spiral)"/><rect x="6" y="0" width="2" height="14" fill="var(--spiral)"/><circle cx="5" cy="16" r="1.6" fill="var(--spiral)"/></pattern></defs>
    <rect width="298" height="20" fill="url(#ring-wide)"/>
  </svg>
  <div class="brand"><span class="brand-dot"></span>lumenforge</div>
  <div class="rule" style="left:19px;right:13px;top:85px"></div>
  <div class="rule" style="left:19px;right:13px;top:107px"></div>
  <div class="rule" style="left:19px;right:13px;top:130px"></div>
  <div class="rule" style="left:19px;right:13px;top:153px"></div>
  <div class="rule" style="left:19px;right:13px;top:175px"></div>
  <div class="rule" style="left:19px;right:13px;top:194px"></div>
</section>

<section class="notepad notepad-tall">
  <svg class="binding" viewBox="0 0 183 20" preserveAspectRatio="none">
    <defs><pattern id="ring-tall" width="12.6" height="20" patternUnits="userSpaceOnUse"><rect x="2" y="0" width="2" height="14" fill="var(--spiral)"/><rect x="6" y="0" width="2" height="14" fill="var(--spiral)"/><circle cx="5" cy="16" r="1.6" fill="var(--spiral)"/></pattern></defs>
    <rect width="183" height="20" fill="url(#ring-tall)"/>
  </svg>
  <div class="brand"><span class="brand-dot"></span>lumenforge</div>
  <div class="rule" style="left:19px;right:18px;top:54px"></div>
  <div class="rule" style="left:19px;right:18px;top:70px"></div>
  <div class="rule" style="left:19px;right:18px;top:86px"></div>
  <div class="rule" style="left:19px;right:18px;top:101px"></div>
  <div class="rule" style="left:19px;right:18px;top:117px"></div>
  <div class="rule" style="left:19px;right:18px;top:132px"></div>
  <div class="rule" style="left:19px;right:18px;top:148px"></div>
  <div class="rule" style="left:19px;right:18px;top:164px"></div>
  <div class="rule" style="left:19px;right:18px;top:179px"></div>
  <div class="rule" style="left:19px;right:18px;top:195px"></div>
  <div class="rule" style="left:19px;right:18px;top:210px"></div>
  <div class="rule" style="left:19px;right:18px;top:226px"></div>
  <div class="rule" style="left:19px;right:18px;top:241px"></div>
</section>

<section class="envelope-back">
  <svg class="flap" width="545" height="92" viewBox="0 0 545 92">
    <path d="M0 0 H545 L536 62 Q532 92 500 92 H45 Q14 92 9 62 Z" fill="var(--orange)"/>
  </svg>
  <div class="flap-web">www.lumenforge.co</div>
  <div class="flap-mark"></div>
</section>

<section class="envelope-front">
  <div class="brand"><span class="brand-dot"></span>lumenforge</div>
  <p class="return-address">412 Copperfield Road<br>Brookhaven, Oregon 97021</p>
  <svg class="corner" width="165" height="130" viewBox="0 0 165 130">
    <path d="M0 130 C20 55 80 4 165 2 V130 Z" fill="var(--orange)"/>
    <path d="M4 130 C24 58 83 7 165 5 V130 Z" fill="var(--blue)"/>
  </svg>
  <div class="front-web">www.lumenforge.co</div>
</section>

</body>
</html>
```